Clear Path Glass Fix Business Card Design Project

Clear Path Glass Fix partners with insurance companies to repair the rock chips and small cracks on automobile windshields.
Updates

Project Deadline Extended Reason: I am going to guarantee payment and would like a few more quality designs. Added Friday, April 21, 2017

Target Market(s)

Will Be placed on windshield with chips. Design to get them to call us.

Industry/Entity Type

Automotive

Contact Information for Business Card

The cards will be placed on windshields near chips in the glass. The FRONT should have a photo of a star type rock chip. Clear Path Glass Fix is happy to provide FREE* rock chip repairs 951 286-4507 The BACK of the card will read. *Clear Path has partnered with over 100 insurance companies to provide
FREE Rock chip repairs to over 80% of our clients.
Why would we do this?
- FOR YOUR VISION AND SAFETY FIRST.
- To prevent crack spreading resulting in a very expensive windshield replacement.
- To preserve your factory set windshield seal.
- To preserve the environment as windshields cannot be recycled.
- To restore the beauty of your vehicle.
ZERO deductible and ZERO effect on your future premiums. CALL TODAY and we will have you Clearing Path in a matter of minutes.

Colors

Designer to choose colors to be used in the design.

Requirements
Must have
• STAR CRACK
Nice to have
• The bullet points on the back could possibly be little star cracks.

```html
<!DOCTYPE html>
<html lang="en">
<head>
<meta charset="utf-8">
<title>Clear Path Glass Fix – Business Card</title>
<link href="https://fonts.googleapis.com/css2?family=Open+Sans:wght@400;600;700&display=swap" rel="stylesheet">
<style>
  :root {
    --page-bg: #e6e7e9;
    --card-bg: #ffffff;
    --ink: #3a3d42;
    --ink-strong: #26282c;
    --accent: #4cc3ec;
    --glass-light: #eef3f7;
    --glass-mid: #b9c3cb;
    --glass-dark: #4a4d52;
  }
  * { box-sizing: border-box; margin: 0; padding: 0; }
  html, body {
    width: 1200px; height: 1200px; overflow: hidden;
    background: var(--page-bg);
    font-family: "Open Sans", sans-serif;
  }
  .sheet {
    width: 1200px; height: 1200px;
    display: flex; flex-direction: column; align-items: center; justify-content: center;
    gap: 60px;
  }
  .card {
    width: 840px; height: 480px;
    background: var(--card-bg);
    box-shadow: 0 6px 18px rgba(0,0,0,0.12);
    position: relative; overflow: hidden;
  }
  /* Front */
  .card-front { background: linear-gradient(100deg, #ffffff 60%, #eaf5fb 100%); }
  .crack-photo {
    position: absolute; left: 250px; top: 20px; width: 380px; height: 220px;
    background: radial-gradient(ellipse at 50% 50%, var(--glass-dark) 0 7%, var(--glass-mid) 16%, var(--glass-light) 40%, rgba(255,255,255,0) 68%);
  }
  .front-copy {
    position: absolute; left: 50px; right: 50px; top: 262px;
    text-align: center;
  }
  .front-offer { font-size: 25px; font-weight: 400; color: var(--ink); }
  .front-phone { margin-top: 12px; font-size: 46px; font-weight: 700; color: var(--ink-strong); letter-spacing: 0.5px; }
  /* Back */
  .card-back {
    display: flex; flex-direction: column; align-items: center; justify-content: center;
    text-align: center; padding: 30px 50px;
  }
  .back-intro { font-size: 17px; color: var(--ink); line-height: 1.45; }
  .back-heading { margin: 12px 0 8px; font-size: 27px; font-weight: 700; color: var(--accent); }
  .reasons { list-style: none; font-size: 19px; color: var(--ink-strong); line-height: 1.45; }
  .back-closing { margin-top: 10px; font-size: 19px; color: var(--accent); line-height: 1.45; }
</style>
</head>
<body>
<main class="sheet">
  <section class="card card-front">
    <div class="crack-photo" role="img" aria-label="Photo of a star-shaped rock chip crack in windshield glass"></div>
    <div class="front-copy">
      <p class="front-offer">Clear Path Glass Fix is happy to provide FREE rock chip repairs</p>
      <p class="front-phone">951 286-4507</p>
    </div>
  </section>

  <section class="card card-back">
    <p class="back-intro">Clear Path has partnered with over 100 insurance companies to provide<br>FREE Rock chip repairs to over 80% of our customers.</p>
    <h2 class="back-heading">Why would we do this?</h2>
    <ul class="reasons">
      <li>FOR YOUR SAFETY FIRST</li>
      <li>To avoid a larger crack resulting in a very expensive windshield replacement</li>
      <li>To preserve your factory set windshield seal</li>
      <li>To preserve the environment as windshields cannot be recycled</li>
    </ul>
    <p class="back-closing">ZERO deductible and ZERO effect on your future premiums<br>Call us today to set up your appointment<br>&amp; we can have you Clearing Path in a matter of minutes</p>
  </section>
</main>
</body>
</html>
```